Mental Health care Company in Washington DC

We are a new mental health care services provider in Washington DC. Please look at these sites.
https://marlowbrookpartners.com
https://www.quillstoneinc.com
https://velmarsh-kt.org/
https://www.trivanqx.com
https://www.thelanternofqz.com

```html
<!DOCTYPE html>
<html lang="en">
<head>
<meta charset="utf-8">
<title>Tovra Health Services</title>
<link rel="stylesheet" href="https://fonts.googleapis.com/css2?family=Mulish:wght@400;500;600;700&family=Roboto+Condensed:wght@700&family=Arimo:wght@400&display=swap">
<style>
:root{
  --navy:#12284a;
  --navy-deep:#0c2244;
  --teal:#a9dcd9;
  --teal-line:#b8dcdc;
  --hero:#b7ddd2;
  --orange:#f4a45d;
  --cream:#fdf6f1;
  --mint:#f1f8f8;
  --peach:#fdf0e8;
  --text:#1f2a3a;
  --muted:#9aa3ad;
  --white:#ffffff;
}
*{box-sizing:border-box;margin:0;padding:0}
html,body{width:1200px;height:3621px;overflow:hidden;background:var(--white)}
body{font-family:"Mulish",sans-serif;color:var(--text);position:relative}
section,header,footer{position:relative;width:1200px}
.abs{position:absolute}
.btn{position:absolute;display:flex;align-items:center;justify-content:center;border-radius:22px;background:var(--teal);color:var(--navy);font-size:16px;font-weight:500;height:42px}
.rule{display:block;width:50px;height:2px;background:#c9ccd1;margin-top:10px}
.body-copy{font-family:"Arimo",sans-serif;font-size:12.2px;line-height:23px;color:#222}

/* header */
.site-header{height:88px;background:var(--white)}
.topbar{left:597px;top:0;width:603px;height:35px;background:var(--navy-deep);clip-path:polygon(22px 0,100% 0,100% 100%,0 100%);display:flex;align-items:center;padding-left:48px;color:var(--white);font-size:13px;gap:14px}
.topbar .phone{color:var(--orange);font-size:15px;display:flex;align-items:center;gap:6px}
.social{display:flex;gap:8px}
.social span{width:23px;height:23px;border-radius:50%;background:#7fb3d9;display:block}
.brand{left:142px;top:14px;display:flex;align-items:center;gap:10px}
.brand .dot{width:14px;height:14px;border-radius:50%;background:var(--orange)}
.brand .name{font-size:30px;font-weight:600;color:var(--navy);letter-spacing:-.5px}
.brand-sub{left:142px;top:60px;font-size:14px;letter-spacing:9px;color:#8a9aaa;font-weight:500}
.nav{right:142px;top:58px;display:flex;gap:38px;font-size:13.5px;font-weight:600;color:var(--navy)}

/* hero */
.hero{height:530px;background:var(--hero)}
.hero h1{left:143px;top:112px;font-family:"Roboto Condensed",sans-serif;font-size:59px;line-height:60px;color:var(--navy);font-weight:700}
.hero .btn{left:141px;top:303px;width:127px;height:42px;background:var(--orange);font-size:16px}
.hero .call-label{left:152px;top:358px;font-size:13px;color:var(--navy)}
.hero .call-num{left:150px;top:380px;font-size:22px;color:var(--navy);display:flex;align-items:center;gap:8px}
.hero-photo{left:675px;top:0;width:525px;height:530px;background:radial-gradient(ellipse at 52% 55%,#e7b89f 0%,#d69a7e 30%,#9ccac0 62%,var(--hero) 80%)}

/* welcome */
.welcome{height:574px}
.welcome .mosaic{left:140px;top:82px}
.welcome .eyebrow{left:598px;top:86px;font-size:25px;color:var(--navy);font-weight:500}
.welcome h2{left:598px;top:112px;font-size:39px;color:var(--navy);font-weight:500}
.welcome .rule{position:absolute;left:598px;top:153px}
.welcome .sub1{left:598px;top:176px;font-size:16px;color:var(--navy);font-weight:500}
.welcome .p1{left:598px;top:203px;width:460px}
.welcome .sub2{left:598px;top:308px;font-size:16px;color:var(--navy);font-weight:500}
.welcome .p2{left:598px;top:335px;width:470px}
.welcome .btn{left:598px;top:448px;width:127px}

/* services */
.services{height:576px;background:var(--cream)}
.services .eyebrow{left:0;width:1200px;text-align:center;top:80px;font-size:24px;color:var(--navy);font-weight:500}
.services h2{left:0;width:1200px;text-align:center;top:104px;font-size:39px;color:var(--navy);font-weight:500}
.services .rule{position:absolute;left:575px;top:148px}
.card{position:absolute;background:var(--white);display:flex;gap:18px;padding:18px 18px 0 22px}
.card.orange{border:1px solid #f4c49c}
.card.teal{border:1px solid var(--teal-line)}
.card .icon{flex:none;width:50px;height:50px;border-radius:50%;background:var(--white);box-shadow:0 2px 8px rgba(0,0,0,.12);margin-top:12px;display:flex;align-items:center;justify-content:center}
.card h3{font-size:13px;font-weight:600;color:#111;margin-bottom:6px}
.card p{font-family:"Arimo",sans-serif;font-size:12px;line-height:20.5px;color:#333}
.hub{left:561px;top:268px;width:76px;height:76px;border-radius:50%;background:var(--white);box-shadow:0 2px 10px rgba(0,0,0,.08)}
.services .btn{left:534px;top:456px;width:127px}

/* first step */
.first-step{height:536px}
.first-step h2{left:142px;top:124px;font-size:32px;color:var(--navy);font-weight:500}
.first-step .rule{position:absolute;left:142px;top:160px}
.first-step .intro{left:142px;top:178px;width:420px;font-size:12.5px;line-height:23px}
.contact-list{left:142px;top:260px;list-style:none;font-size:13.5px;font-weight:600;color:#1b1b1b}
.contact-list li{display:flex;align-items:center;gap:15px;height:32.5px}
.first-step .btn{left:142px;top:360px;width:177px}
.first-step .photo{left:614px;top:77px;width:445px;height:383px;background:linear-gradient(100deg,#c9cfcd 0%,#e8e4df 40%,#d9dcd6 65%,#9da89a 100%)}

/* rooted */
.rooted{height:389px;background:var(--mint)}
.rooted .illus{left:56px;top:70px;width:534px;height:253px;background:radial-gradient(ellipse at 50% 45%,#3f9aa8 0%,#a7d6d9 35%,#d6ecee 60%,var(--mint) 80%)}
.rooted h2{left:610px;top:72px;font-size:39px;line-height:40px;color:var(--navy);font-weight:500}
.rooted .p{left:614px;top:170px;width:430px}
.rooted .btn{left:610px;top:276px;width:177px}

/* contact */
.contact{height:770px;background:linear-gradient(180deg,#2d64a8 0%,#5d8fc4 30%,#8aa7b8 48%,#6b7c6b 70%,#44604a 86%,#2d4b5a 100%)}
.contact h2{left:0;width:1200px;text-align:center;top:80px;font-size:39px;color:var(--white);font-weight:500}
.contact .rule-w{left:575px;top:134px;width:50px;height:2px;background:var(--white)}
.contact .lede{left:180px;top:150px;width:840px;text-align:center;font-size:12px;line-height:23px;color:var(--white);font-weight:600}
.panel{left:183px;top:232px;width:831px;height:444px;display:flex}
.panel .details{width:415px;background:var(--peach);padding:50px 33px}
.panel .inquiry{flex:1;background:var(--white);padding:50px 40px 0 36px}
.panel h3{font-size:21px;font-weight:500;color:#1b1b1b}
.panel .rule{margin-bottom:22px}
.details .note{font-size:11.5px;line-height:22px;color:#333;margin-bottom:18px}
.info-row{display:flex;align-items:center;gap:17px;font-size:13px;line-height:20px;color:#222;margin-bottom:14px}
.info-row .ic{width:34px;height:34px;border-radius:50%;background:var(--orange);flex:none;display:flex;align-items:center;justify-content:center}
.follow{display:flex;align-items:center;gap:6px;font-size:16px;font-weight:600;margin-top:30px}
.follow span{width:28px;height:28px;border-radius:50%;background:var(--navy-deep)}
.field{display:flex;align-items:center;gap:8px;font-size:12px;color:#444;border-bottom:1px solid #9a9a9a;height:48px;padding-top:10px;width:337px}
.field.msg{height:78px;align-items:flex-start;padding-top:28px}
.inquiry .btn{position:relative;margin-top:30px;width:99px;height:38px;font-size:16px}

/* footer */
.site-footer{height:113px}
.site-footer .brand{left:140px;top:30px}
.site-footer .brand .name{font-size:38px}
.site-footer .brand-sub{left:140px;top:80px;font-size:16px}
.site-footer .nav{top:55px}
.copyright{height:45px;background:var(--navy-deep);color:#c9d1dc;font-size:12.5px;display:flex;align-items:center;justify-content:center}
</style>
</head>
<body>

<header class="site-header">
  <div class="abs topbar">
    <span>For More Information Call Us Today</span>
    <span class="phone"><svg width="15" height="15" viewBox="0 0 24 24" fill="none" stroke="#f4a45d" stroke-width="2"><path d="M5 3h4l2 5-3 2a12 12 0 0 0 6 6l2-3 5 2v4a2 2 0 0 1-2 2A17 17 0 0 1 3 5a2 2 0 0 1 2-2z"/></svg>123.456.7890</span>
    <span class="social"><span></span><span></span></span>
  </div>
  <div class="abs brand"><span class="name">Tovra Health</span><span class="dot"></span></div>
  <div class="abs brand-sub">SERVICES</div>
  <nav class="abs nav"><span>Home</span><span>About Us</span><span>Services We Provide</span><span>Employment</span><span>Contact Us</span></nav>
</header>

<section class="hero">
  <div class="abs hero-photo" role="img" aria-label="Hands holding a paper head cut-out with a colourful brain illustration"></div>
  <h1 class="abs">Invest In Yourself<br>- It Starts With<br>Your Mind</h1>
  <a class="btn">Know More</a>
  <div class="abs call-label">For More Information Call Us Today</div>
  <div class="abs call-num"><svg width="26" height="26" viewBox="0 0 24 24" fill="none" stroke="#12284a" stroke-width="1.5"><path d="M5 3h4l2 5-3 2a12 12 0 0 0 6 6l2-3 5 2v4a2 2 0 0 1-2 2A17 17 0 0 1 3 5a2 2 0 0 1 2-2z"/></svg>123.456.7890</div>
</section>

<section class="welcome">
  <svg class="abs mosaic" width="418" height="414" viewBox="0 0 418 414" role="img" aria-label="Photo mosaic of a smiling woman and a counselling session">
    <defs>
      <linearGradient id="g1" x1="0" y1="0" x2="0" y2="1"><stop offset="0" stop-color="#9fcbd0"/><stop offset="1" stop-color="#c08a66"/></linearGradient>
      <linearGradient id="g2" x1="0" y1="0" x2="1" y2="0"><stop offset="0" stop-color="#e3b89a"/><stop offset="1" stop-color="#c88958"/></linearGradient>
      <linearGradient id="g3" x1="0" y1="0" x2="1" y2="1"><stop offset="0" stop-color="#d7e6ea"/><stop offset="1" stop-color="#8fbcc7"/></linearGradient>
      <linearGradient id="g4" x1="0" y1="0" x2="0" y2="1"><stop offset="0" stop-color="#c99f85"/><stop offset="1" stop-color="#8a6a58"/></linearGradient>
    </defs>
    <path d="M163 45a45 45 0 0 1 90 0v117h-90z" fill="url(#g1)"/>
    <path d="M163 162v90H45a45 45 0 0 1 0-90z" fill="url(#g2)"/>
    <path d="M253 162h120a45 45 0 0 1 0 90H253z" fill="url(#g3)"/>
    <path d="M163 252h90v117a45 45 0 0 1-90 0z" fill="url(#g4)"/>
  </svg>
  <div class="abs eyebrow">Welcome to</div>
  <h2 class="abs">Tovra Health Services</h2>
  <span class="rule"></span>
  <div class="abs sub1">Compassionate Mental Health Care in Washington, DC</div>
  <p class="abs body-copy p1">At Tovra Health Services, we believe that mental wellness is essential to living a full and meaningful life. Located in the heart of Washington, DC, our practice is committed to supporting individuals, couples, and families on their journey to emotional well-being.</p>
  <div class="abs sub2">Your Partner in Healing &amp; Growth</div>
  <p class="abs body-copy p2">Whether you're navigating anxiety, depression, trauma, relationship challenges, or simply looking for support in life transitions, our team of licensed mental health professionals is here to help. We provide a safe, inclusive, and confidential space where you can feel heard, respected, and empowered to heal</p>
  <a class="btn">Know More</a>
</section>

<section class="services">
  <div class="abs eyebrow">Our Specialties</div>
  <h2 class="abs">Services We Provide</h2>
  <span class="rule"></span>
  <div class="card orange" style="left:140px;top:186px;width:447px;height:113px">
    <span class="icon"><svg width="26" height="26" viewBox="0 0 24 24" fill="none" stroke="#12284a" stroke-width="1.4"><circle cx="6" cy="7" r="2.5"/><circle cx="18" cy="7" r="2.5"/><path d="M2 20v-6h8v6M14 20v-6h8v6"/></svg></span>
    <div><h3>Individual Therapy</h3><p>Ut wisi enim ad minim veniam, quis nostrud exerci tation ullamcorper suscipit lobortis nisl ut aliquip ex ea commodo consequat.</p></div>
  </div>
  <div class="card teal" style="left:621px;top:186px;width:438px;height:113px">
    <span class="icon"><svg width="26" height="26" viewBox="0 0 24 24" fill="none" stroke="#12284a" stroke-width="1.4"><circle cx="7" cy="6" r="2.3"/><circle cx="17" cy="6" r="2.3"/><circle cx="12" cy="11" r="2"/><path d="M3 20h18M5 20v-5M19 20v-5"/></svg></span>
    <div><h3>Couples &amp; Family Counseling</h3><p>Ut wisi enim ad minim veniam, quis nostrud exerci tation ullamcorper suscipit lobortis nisl ut aliquip ex ea commodo consequat.</p></div>
  </div>
  <div class="card teal" style="left:140px;top:313px;width:447px;height:112px">
    <span class="icon"><svg width="26" height="26" viewBox="0 0 24 24" fill="none" stroke="#12284a" stroke-width="1.4"><path d="M6 20v-4a7 7 0 1 1 10 0v4"/><circle cx="11" cy="10" r="3" stroke="#f4a45d"/></svg></span>
    <div><h3>Psychiarty</h3><p>Ut wisi enim ad minim veniam, quis nostrud exerci tation ullamcorper suscipit lobortis nisl ut aliquip ex ea commodo consequat.</p></div>
  </div>
  <div class="card orange" style="left:621px;top:313px;width:438px;height:112px">
    <span class="icon"><svg width="26" height="26" viewBox="0 0 24 24" fill="none" stroke="#12284a" stroke-width="1.4"><circle cx="8" cy="5" r="2" stroke="#f4a45d"/><circle cx="16" cy="5" r="2" stroke="#f4a45d"/><path d="M3 21v-7l4 3M21 21v-7l-4 3M8 9v5M16 9v5"/></svg></span>
    <div><h3>Community Support Services</h3><p>Ut wisi enim ad minim veniam, quis nostrud exerci tation ullamcorper suscipit lobortis nisl ut aliquip ex ea commodo consequat.</p></div>
  </div>
  <div class="abs hub"></div>
  <a class="btn">Know More</a>
</section>

<section class="first-step">
  <h2 class="abs">Take the First Step Today</h2>
  <span class="rule"></span>
  <p class="abs intro">Seeking support is a sign of strength. If you're ready to begin your journey toward healing, we're here to walk with you every step of the way.</p>
  <ul class="abs contact-list">
    <li><svg width="18" height="18" viewBox="0 0 24 24" fill="none" stroke="#f4a45d" stroke-width="1.6"><path d="M5 3h4l2 5-3 2a12 12 0 0 0 6 6l2-3 5 2v4a2 2 0 0 1-2 2A17 17 0 0 1 3 5a2 2 0 0 1 2-2z"/></svg>Call us at 123.456.7890</li>
    <li><svg width="18" height="18" viewBox="0 0 24 24" fill="none" stroke="#f4a45d" stroke-width="1.6"><path d="M12 22s7-7 7-12a7 7 0 0 0-14 0c0 5 7 12 7 12z"/><circle cx="12" cy="10" r="2.5"/></svg>Visit us at : Street Name, City Name, State Zipcode</li>
    <li><svg width="18" height="18" viewBox="0 0 24 24" fill="none" stroke="#f4a45d" stroke-width="1.6"><rect x="3" y="5" width="18" height="16" rx="2"/><path d="M3 10h18M8 3v4M16 3v4"/></svg>Schedule an appointment online</li>
  </ul>
  <a class="btn">Contact Us Today</a>
  <div class="abs photo" role="img" aria-label="Therapist with clipboard listening to a young woman client in a bright office"></div>
</section>

<section class="rooted">
  <div class="abs illus" role="img" aria-label="Illustration of a diverse care team around a puzzle-piece brain with a heart, framed by leaves"></div>
  <h2 class="abs">Rooted in Community,<br>Guided by Care</h2>
  <p class="abs body-copy p">As part of the vibrant and diverse DC community, we honor the unique experiences of every individual we serve. Our team brings cultural competence, evidence-based practices, and a deep commitment to mental health equity.</p>
  <a class="btn">Contact Us Today</a>
</section>

<section class="contact" role="img" aria-label="Aerial view of Washington, DC under a blue sky">
  <h2 class="abs">Contact Us</h2>
  <div class="abs rule-w"></div>
  <p class="abs lede">Have questions or need help getting started? Our team is here to support you. Reach out today — whether you're looking to schedule an appointment, learn more about our services, or simply talk to someone who cares.</p>
  <div class="abs panel">
    <div class="details">
      <h3>Contact Details</h3>
      <span class="rule"></span>
      <p class="note">Every message is confidential, and we're committed to responding promptly.</p>
      <div class="info-row"><span class="ic"><svg width="16" height="16" viewBox="0 0 24 24" fill="none" stroke="#12284a" stroke-width="1.8"><path d="M12 22s7-7 7-12a7 7 0 0 0-14 0c0 5 7 12 7 12z"/><circle cx="12" cy="10" r="2.5"/></svg></span><span>Street Name, City Name<br>State Zipcode</span></div>
      <div class="info-row"><span class="ic"><svg width="16" height="16" viewBox="0 0 24 24" fill="none" stroke="#12284a" stroke-width="1.8"><rect x="3" y="6" width="18" height="13" rx="1"/><path d="M3 7l9 7 9-7"/></svg></span><span>info@marenvale.com</span></div>
      <div class="info-row"><span class="ic"><svg width="16" height="16" viewBox="0 0 24 24" fill="none" stroke="#12284a" stroke-width="1.8"><path d="M5 3h4l2 5-3 2a12 12 0 0 0 6 6l2-3 5 2v4a2 2 0 0 1-2 2A17 17 0 0 1 3 5a2 2 0 0 1 2-2z"/></svg></span><span>123-456-7890</span></div>
      <div class="follow">Follow Us:&nbsp;<span></span><span></span></div>
    </div>
    <div class="inquiry">
      <h3>Quick Inquiry</h3>
      <span class="rule"></span>
      <div class="field"><svg width="14" height="14" viewBox="0 0 24 24" fill="none" stroke="#f4a45d" stroke-width="1.8"><circle cx="12" cy="8" r="4"/><path d="M4 21a8 8 0 0 1 16 0"/></svg>Name</div>
      <div class="field"><svg width="14" height="14" viewBox="0 0 24 24" fill="none" stroke="#f4a45d" stroke-width="1.8"><rect x="3" y="6" width="18" height="13" rx="1"/><path d="M3 7l9 7 9-7"/></svg>Email</div>
      <div class="field"><svg width="14" height="14" viewBox="0 0 24 24" fill="none" stroke="#f4a45d" stroke-width="1.8"><path d="M5 3h4l2 5-3 2a12 12 0 0 0 6 6l2-3 5 2v4a2 2 0 0 1-2 2A17 17 0 0 1 3 5a2 2 0 0 1 2-2z"/></svg>Phone</div>
      <div class="field msg"><svg width="14" height="14" viewBox="0 0 24 24" fill="none" stroke="#f4a45d" stroke-width="1.8"><path d="M4 5h16v11H9l-5 4z"/></svg>Message</div>
      <a class="btn">Submit</a>
    </div>
  </div>
</section>

<footer class="site-footer">
  <div class="abs brand"><span class="name">Tovra Health</span><span class="dot"></span></div>
  <div class="abs brand-sub">SERVICES</div>
  <nav class="abs nav"><span>Home</span><span>About Us</span><span>Services We Provide</span><span>Employment</span><span>Contact Us</span></nav>
</footer>
<div class="copyright">© 2025. Tovra Health Services.&nbsp; All Rights Reserved.</div>

</body>
</html>
```